■依頼の目的/概要
池袋、渋谷にある猫カフェ「PuRLi」の
店頭看板用ポスターを作成して頂きたいです。

■PuRLi概要

PuRLiは渋谷・池袋にある猫カフェです。
http://cafepurli.jp/

-最近、猫と遊んだことありますか?-

猫をなでたり、一緒に遊んだり、
PuRLiは猫たちとの癒しの時間をゆったりと過ごせる空間を提供しております。

池袋店は、木のぬくもりが感じられるこだわりの内装と明るい店内。
元気一杯の猫ちゃんたちと触れ合えるお店です。

新たにオープンした渋谷店は
都会の喧騒を忘れさせる落ち着いた店内が特長。
店舗が8・9階なので渋谷が一望できる最高の見晴らし&落ち着いた空間で
猫たちと触れ合うことができます。

内装だけでなく、においなどの衛生面に配慮し、
従来の猫カフェのイメージを払拭すべく、おしゃれで誰でも立ち寄れる猫カフェを目指しています。

おしゃれな猫カフェとして
様々なメディアにも取り上げられております。

プレスリリース
http://newswirez.jp/main/html/rd/p/000000001.000014659.html

まるでバーのような猫カフェ
http://news.tabiroute.jp/news/2015/07/23/340/

おしゃれ過ぎる大人の猫カフェ
http://beauty.kumoraku.co.jp/buzz/articles/216875

POKOニュース
http://news.poko.me/issue/odekake/ae588d362140

もっふもふに勝る癒しなし?
http://hu-t.me/article/173012970747529840

ヨリドリ!
http://www.yori-dori.com/content/11601/

聞いてPIKO
http://kiite.piko.ne.jp/watch/entry/675b5c9870a0e51eccd6b58452015943/

■依頼詳細

・サイズ
B1:横幅(mm)728、高さ(mm)1030

記載事項
・PuRLiロゴ
・キャッチコピー(仮)
「最近、猫と遊んだことありますか?」
・当ビル8階
・OPEN 10:00~22:00(最終入店21:30)
・10分 200円(税別)

・ドリンクバー ¥350(税別)
・漫画 雑誌
・Wi-Fi
・電源/コンセント

・中学生以上入場可能
・電話番号:03-5812-7740
・English OK
・中文 OK
・URL:cafepurli.jp/

※言い回しや表記は意味合いが変わらないようであれば
日本語・英語表記の変更OKです。

★ロゴデータを添付しておりますのでご使用下さい。
猫の参考、素材写真は下記URLよりダウンロード可能です。
http://11.sendraku.nu/h7b911505013ee928d2f67a1ce7fb821d-0925

■納品ファイル
・高解像度JPG (.jpg)
・イラストレーター形式 (.ai)

■重視する点

街を歩いているときに目を引く、PuRLiへ行ってみたいと思わせる、
ついつい足をとめて見てしまうようなデザインを求めています。

渋谷・池袋の両店舗前に設置する店頭ポスター(看板)として使用いたします。
デザインの決定後、記載情報などの変更をお願いをいたします。

写真とキャッチの魅せ方
文字情報のメリハリ
情報の伝わりやすさ
目を惹く素晴らしいデザインでした。

この度は猫カフェの店頭ポスターへご提案頂き、ありがとうござました。
予想を遥かに越えるご提案数に加え、レベルの高いデザインが多く、
選考に困難を極めました。
沢山のご提案感謝いたします。
次の機会もぜひよろしくお願いいたします。

```html
<!DOCTYPE html>
<html lang="ja">
<head>
<meta charset="utf-8">
<title>猫カフェ PuRLi 店頭ポスター</title>
<link rel="stylesheet" href="https://fonts.googleapis.com/css2?family=Noto+Sans+JP:wght@400;500;700&family=Noto+Serif+JP:wght@400;500&display=swap">
<style>
  :root {
    --ink-white: #ffffff;
    --ink-soft: #f4efe7;
    --bg-deep: #0d0907;
    --bg-brown: #2c1c11;
    --brick: #5a3520;
    --lamp-glow: #d7ab72;
    --lamp-core: #fbeccd;
    --cushion: #b8a38a;
    --cushion-dark: #6f5c49;
    --cat-fur: #c2a78a;
    --cat-shade: #7d6550;
    --text-shadow: 0 2px 6px rgba(0,0,0,0.75);
  }
  * { margin: 0; padding: 0; box-sizing: border-box; }
  html, body { width: 849px; height: 1200px; overflow: hidden; background: var(--bg-deep); }
  .poster {
    position: relative;
    width: 849px;
    height: 1200px;
    overflow: hidden;
    color: var(--ink-white);
    font-family: "Noto Sans JP", sans-serif;
    text-shadow: var(--text-shadow);
  }
  .scene-photo {
    position: absolute; inset: 0;
    background:
      radial-gradient(ellipse 120px 90px at 560px 470px, rgba(255,240,210,0.55) 0%, rgba(255,240,210,0) 100%),
      radial-gradient(ellipse 230px 150px at 620px 300px, var(--lamp-core) 0%, var(--lamp-glow) 45%, rgba(120,80,45,0) 100%),
      radial-gradient(ellipse 110px 200px at 650px 930px, var(--cat-fur) 0%, var(--cat-shade) 55%, rgba(70,50,35,0) 100%),
      radial-gradient(ellipse 90px 110px at 660px 1100px, #d9c8b2 0%, rgba(120,100,80,0) 100%),
      radial-gradient(ellipse 220px 250px at 340px 830px, var(--cushion) 0%, var(--cushion-dark) 55%, rgba(60,45,35,0) 100%),
      radial-gradient(ellipse 180px 320px at 780px 900px, #4a3e34 0%, rgba(40,30,25,0) 100%),
      radial-gradient(ellipse 260px 420px at 250px 420px, var(--brick) 0%, rgba(60,35,20,0) 100%),
      linear-gradient(180deg, var(--bg-deep) 0%, var(--bg-brown) 40%, #1a110b 100%);
  }
  .floor-info { position: absolute; right: 22px; top: 22px; text-align: right; }
  .floor-info .floor { font-size: 34px; font-weight: 500; letter-spacing: 2px; }
  .floor-info .hours { font-size: 32px; font-weight: 500; margin-top: 30px; letter-spacing: 3px; }
  .floor-info .last-entry { font-size: 30px; margin-top: 4px; margin-right: 34px; letter-spacing: 2px; }
  .catch-copy {
    position: absolute; top: 262px; left: 0; width: 849px;
    text-align: center;
    font-family: "Noto Serif JP", serif;
    font-weight: 500;
    font-size: 34px; letter-spacing: 3px;
    color: var(--ink-soft);
  }
  .brand { position: absolute; left: 170px; top: 415px; display: flex; align-items: center; gap: 60px; }
  .brand-dot { width: 170px; height: 170px; border-radius: 50%; border: 5px solid var(--ink-white); }
  .brand-name { font-size: 92px; font-weight: 700; letter-spacing: 6px; line-height: 1; margin-top: 70px; }
  .menu { position: absolute; left: 18px; top: 620px; }
  .section-label {
    font-size: 32px; font-weight: 500; letter-spacing: 2px;
    padding-bottom: 6px; border-bottom: 3px solid var(--ink-white);
    width: 400px;
  }
  .menu-item { font-size: 38px; font-weight: 500; margin-top: 6px; }
  .menu-item.price-time { padding-left: 34px; }
  .menu-item small { font-size: 34px; }
  .free { position: absolute; left: 18px; top: 800px; }
  .free .section-label { width: 280px; }
  .free ul { list-style: none; margin-top: 12px; }
  .free li { font-size: 25px; line-height: 37px; padding-left: 22px; }
  .free li::before { content: "◎"; margin-right: 22px; }
  .welcome-badge { position: absolute; left: 2px; top: 978px; width: 340px; height: 180px; }
  .welcome-text {
    position: absolute; left: 2px; top: 994px; width: 340px;
    text-align: center; line-height: 1.12;
  }
  .welcome-text .lang { font-size: 42px; font-weight: 700; }
  .welcome-text .age { font-size: 27px; font-weight: 700; margin-top: 2px; }
  .shop-contact { position: absolute; right: 22px; top: 1112px; text-align: right; }
  .shop-contact .shop-name { font-size: 26px; }
  .shop-contact .lines { font-size: 24px; margin-top: 10px; letter-spacing: 1px; }
</style>
</head>
<body>
<main class="poster">
  <div class="scene-photo" role="img" aria-label="薄暗いシックな店内、煉瓦の壁と灯りのともるランプ、クッションを置いたソファ、その前にちょこんと座る猫の写真"></div>

  <section class="floor-info">
    <p class="floor">当ビル 8F</p>
    <p class="hours">OPEN　10:00～22:00</p>
    <p class="last-entry">（最終入店　21:30）</p>
  </section>

  <h2 class="catch-copy">最近、猫と遊んだことありますか？</h2>

  <div class="brand">
    <span class="brand-dot"></span>
    <h1 class="brand-name">PuRLi</h1>
  </div>

  <section class="menu">
    <p class="section-label">メニュー Menu</p>
    <p class="menu-item price-time">10min.　¥200<small>（税別）</small></p>
    <p class="menu-item">ドリンクバー¥350<small>（税別）</small></p>
  </section>

  <section class="free">
    <p class="section-label">フリー Free</p>
    <ul>
      <li>漫画・雑誌</li>
      <li>Wi-Fi</li>
      <li>電源／コンセント</li>
    </ul>
  </section>

  <svg class="welcome-badge" viewBox="0 0 340 180" aria-hidden="true">
    <ellipse cx="170" cy="90" rx="164" ry="84" fill="rgba(0,0,0,0.35)" stroke="#ffffff" stroke-width="4"/>
  </svg>
  <div class="welcome-text">
    <p class="lang">English OK</p>
    <p class="lang">中文 OK</p>
    <p class="age">中学生以上入場可</p>
  </div>

  <footer class="shop-contact">
    <p class="shop-name">猫カフェ　PuRLi</p>
    <p class="lines">Tel : 03-5812-7740　URL : http://cafepurli.jp/</p>
  </footer>
</main>
</body>
</html>
```